Varnok Develoipment and Management Corp Web Design Project

Website... Based on logo. Update forthcoming....
Updates

Reason: Extended to include recently completed logo design.

Target Market(s)

Financiers, investors, public officials, and landowners.

Industry/Entity Type

Management

Requirements
Should not have
• No palm trees, mayan ruins, or other Caribbean references.

```html
<!DOCTYPE html>
<html lang="en">
<head>
<meta charset="utf-8">
<title>Varnok Develoipment and Management Corp</title>
<link rel="stylesheet" href="https://fonts.googleapis.com/css2?family=Raleway:wght@300;400;500;600&family=Open+Sans:ital,wght@0,400;0,600;0,700;1,400&display=swap">
<style>
:root{
  --navy:#15527a;
  --navy-deep:#0e2d45;
  --ink:#1f2a33;
  --text:#6b6f73;
  --orange:#e3901b;
  --gold:#e29d0c;
  --paper:#ffffff;
  --mist:#f7f7f7;
  --card:rgba(16,44,70,.88);
}
*{margin:0;padding:0;box-sizing:border-box}
html,body{width:1200px;height:2209px;overflow:hidden;background:var(--paper)}
body{position:relative;font-family:"Open Sans",sans-serif;color:var(--text)}
.abs{position:absolute}
.center{text-align:center}

/* header */
.site-header{position:absolute;left:0;top:0;width:1200px;height:91px;background:var(--paper)}
.brand{position:absolute;left:121px;top:20px;font-family:"Raleway",sans-serif;font-weight:500;font-size:38px;color:#134565;letter-spacing:.5px}
.main-nav a{position:absolute;top:38px;font-size:15px;color:var(--ink);text-decoration:none;transform:translateX(-50%);white-space:nowrap}
.main-nav a.is-active{color:var(--orange)}
.nav-marker{position:absolute;left:522px;top:87px;width:64px;height:4px;background:var(--navy)}

/* hero */
.hero{position:absolute;left:0;top:91px;width:1200px;height:520px;background:linear-gradient(100deg,#e9eaeb 0%,#f7f7f7 45%,#eeeeee 100%)}
.hero-caption{position:absolute;left:143px;top:155px;width:414px;height:166px;background:var(--navy);border-bottom:5px solid var(--orange);padding:26px 30px 0}
.hero-caption h1{font-family:"Raleway",sans-serif;font-weight:500;font-size:35px;color:#fff;line-height:1.05}
.hero-caption h2{font-family:"Raleway",sans-serif;font-weight:400;font-size:20px;color:#fff;margin-top:6px}
.hero-caption p{font-size:10px;line-height:15px;color:#b9cbd9;margin-top:8px}
.hero-arrow{position:absolute;top:179px}

/* about */
.about{position:absolute;left:0;top:611px;width:1200px;height:328px;background:var(--paper)}
.section-title{font-family:"Raleway",sans-serif;font-weight:400;color:var(--ink)}
.about h2{position:absolute;left:0;width:1200px;top:52px;font-size:33px}
.about p{position:absolute;left:180px;width:840px;font-size:11px;line-height:18px}
.btn{position:absolute;background:var(--navy);color:#fff;font-weight:700;font-size:13px;text-align:center;line-height:30px;height:30px;text-decoration:none}

/* services */
.services{position:absolute;left:0;top:939px;width:1200px;height:377px;background:var(--gold)}
.services h2{position:absolute;left:0;width:1200px;top:45px;font-family:"Raleway",sans-serif;font-weight:400;font-size:29px;color:#fff}
.service{position:absolute;top:128px;width:237px;margin-left:-118px;text-align:center;color:#fff}
.service svg{display:block;margin:0 auto}
.service h3{font-family:"Raleway",sans-serif;font-weight:400;font-size:19px;margin-top:28px}
.service p{font-size:11px;line-height:18px;color:#fbe6bf;margin:4px 12px 0}
.service a{display:block;font-size:12px;color:#222;text-decoration:none;margin-top:6px}
.divider{position:absolute;top:133px;width:1px;height:191px;background:rgba(255,255,255,.35)}

/* projects */
.projects{position:absolute;left:0;top:1316px;width:1200px;height:388px;background:var(--mist)}
.projects h2{position:absolute;left:121px;top:82px;font-family:"Raleway",sans-serif;font-weight:400;font-size:30px;line-height:36px;color:var(--ink)}
.projects h2 span{color:var(--orange)}
.projects p{position:absolute;left:121px;width:500px;font-size:11px;line-height:18px}
.video-frame{position:absolute;left:685px;top:67px;width:382px;height:242px;background:#fff;border:1px solid #dedede;padding:5px}
.video-still{width:100%;height:100%;background:radial-gradient(ellipse at 55% 45%,#5a5a5a 0%,#2a2a2a 55%,#151515 100%);position:relative}

/* testimonials */
.testimonials{position:absolute;left:0;top:1704px;width:1200px;height:384px;background:linear-gradient(90deg,#2d5a7b 0%,#3c6a8a 50%,#2a5676 100%)}
.testimonials h2{position:absolute;left:0;width:1200px;top:48px;font-family:"Raleway",sans-serif;font-weight:400;font-size:27px;color:#fff}
.quote-card{position:absolute;top:107px;width:282px;height:233px;background:var(--card);text-align:center;padding-top:22px}
.avatar{width:76px;height:76px;border-radius:50%;margin:0 auto;border:3px solid #fff;background:linear-gradient(160deg,#d9d4cf,#8c8580)}
.quote-card blockquote{font-style:italic;font-size:11px;line-height:18px;color:#fff;margin:12px 22px 0}
.quote-card cite{display:block;font-style:normal;font-size:13px;color:#e6edf3;margin-top:6px}

/* footer */
.site-footer{position:absolute;left:0;top:2088px;width:1200px;height:121px;background:var(--navy-deep)}
.footer-nav{position:absolute;left:131px;top:36px;font-size:15px;color:#fff}
.footer-nav a{color:#fff;text-decoration:none}
.footer-nav .sep{margin:0 7px}
.copyright{position:absolute;left:131px;top:68px;font-size:10px;color:#b8c4ce}
.social{position:absolute;right:131px;top:38px;font-size:14px;font-weight:600;color:#fff}
.social span{margin-left:12px}
</style>
</head>
<body>

<header class="site-header">
  <div class="brand">Varnok</div>
  <nav class="main-nav">
    <a class="is-active" style="left:551px">Home</a>
    <a style="left:640px">About Us</a>
    <a style="left:739px">Services</a>
    <a style="left:833px">Projects</a>
    <a style="left:942px">Testimonials</a>
    <a style="left:1051px">Contact</a>
  </nav>
  <div class="nav-marker"></div>
</header>

<section class="hero" role="img" aria-label="Businessman drawing gears labelled goals, strategy, innovation, growth, research and team work on a white wall">
  <svg class="hero-arrow" style="left:62px" width="42" height="92" viewBox="0 0 42 92"><polyline points="40,2 2,46 40,90" fill="none" stroke="#9a9a9a" stroke-width="2"/></svg>
  <svg class="hero-arrow" style="left:1098px" width="42" height="92" viewBox="0 0 42 92"><polyline points="2,2 40,46 2,90" fill="none" stroke="#9a9a9a" stroke-width="2"/></svg>
  <div class="hero-caption">
    <h1>CURABITUR IACULIS</h1>
    <h2>MAURIS VEL LACUS VITAE FELIS</h2>
    <p>us eros Curabitur vel mi sit amet magna malesuada ultrices Ut nisi erat fermentum vel congue id euismod in elit Fusce</p>
  </div>
</section>

<section class="about">
  <h2 class="section-title center">About Our Company &amp; Mission</h2>
  <p class="center" style="top:105px">Morbi diam mauris viverra in gravida eu mattis in ante Morbi eget arcu Morbi porta libero id ullamcorper nonummy nibh ligula pulvinar metus eget consectetuer augue nisi quis lacus Ut ac mi quis lacus mollis aliquam Curabitur iaculis tempus eros Curabitur vel mi sit amet magna malesuada ultrices Ut nisi erat fermentum vel congue id euismod in elit Fusce ultricies orci ac feugiat suscipit leo massa sodales velit et scelerisque mi tortor at ipsum</p>
  <p class="center" style="top:168px">Mauris vel lacus vitae felis vestibulum volutpat Etiam est nunc venenatis in tristique eu imperdiet ac nisl Cum sociis natoque penatibus et magnis dis parturient montes nascetur ridiculus mus In iaculis facilisis massa Etiam eu u</p>
  <a class="btn" style="left:542px;top:216px;width:109px">Read More</a>
</section>

<section class="services">
  <h2 class="center">Services We Provide</h2>
  <div class="divider" style="left:362px"></div>
  <div class="divider" style="left:599px"></div>
  <div class="divider" style="left:836px"></div>

  <div class="service" style="left:244px">
    <svg width="50" height="66" viewBox="0 0 50 66"><path d="M25 4a20 20 0 0 0-12 36c3 3 4 6 4 10h16c0-4 1-7 4-10A20 20 0 0 0 25 4z" fill="none" stroke="#fff" stroke-width="4"/><path d="M18 55h14M19 61h12" stroke="#fff" stroke-width="4" stroke-linecap="round"/><path d="M15 24a10 10 0 0 1 10-10" fill="none" stroke="#fff" stroke-width="3"/></svg>
    <h3>Featured Service</h3>
    <p>Curabitur iaculis tempus eros Curabitur vel mi sit amet magna malesuada ultrices Ut nisi erat fermentum</p>
    <a>Learn More</a>
  </div>
  <div class="service" style="left:481px">
    <svg width="84" height="66" viewBox="0 0 84 66"><rect x="14" y="8" width="56" height="40" rx="3" fill="none" stroke="#fff" stroke-width="4"/><path d="M3 54h78l-4 6H7z" fill="#fff"/></svg>
    <h3>Featured Service</h3>
    <p>Curabitur iaculis tempus eros Curabitur vel mi sit amet magna malesuada ultrices Ut nisi erat fermentum</p>
    <a>Learn More</a>
  </div>
  <div class="service" style="left:718px">
    <svg width="66" height="66" viewBox="0 0 66 66"><path d="M44 6a14 14 0 0 0-12 20L8 50a5 5 0 0 0 8 8l24-24A14 14 0 0 0 60 22l-8 8-10-2-2-10 8-8a14 14 0 0 0-4-4z" fill="#fff"/></svg>
    <h3>Featured Service</h3>
    <p>Curabitur iaculis tempus eros Curabitur vel mi sit amet magna malesuada ultrices Ut nisi erat fermentum</p>
    <a>Learn More</a>
  </div>
  <div class="service" style="left:954px">
    <svg width="70" height="66" viewBox="0 0 70 66"><path d="M5 6v52h60" fill="none" stroke="#fff" stroke-width="4"/><polyline points="12,48 28,30 38,40 56,20" fill="none" stroke="#fff" stroke-width="5"/><path d="M46 16h14v14z" fill="#fff"/></svg>
    <h3>Featured Service</h3>
    <p>Curabitur iaculis tempus eros Curabitur vel mi sit amet magna malesuada ultrices Ut nisi erat fermentum</p>
    <a>Learn More</a>
  </div>
</section>

<section class="projects">
  <h2>Development and<br><span>Management Projects</span></h2>
  <p style="top:163px">Morbi porta libero id ullamcorper nonummy nibh ligula pulvinar metus eget consectetuer augue nisi quis lacus Ut ac mi quis lacus mollis aliquam Curabitur iaculis tempus eros Curabitur vel mi sit amet magna malesuada ultrices Ut nisi erat fermentum</p>
  <p style="top:226px">Fusce ultricies orci ac feugiat suscipit leo massa sodales velit et scelerisque mi tortor at ipsumFusce tellus Sed metus augue convallis et vehicula ut pulvinar eu</p>
  <a class="btn" style="left:122px;top:277px;width:109px">Read More</a>
  <div class="video-frame">
    <div class="video-still" role="img" aria-label="Businessman in a suit sketching a rising bar chart on glass">
      <svg style="position:absolute;left:166px;top:90px" width="44" height="50" viewBox="0 0 44 50"><polygon points="4,2 42,25 4,48" fill="rgba(255,255,255,.85)"/></svg>
    </div>
  </div>
</section>

<section class="testimonials" aria-label="Client testimonials over a photo of business people">
  <h2 class="center">What Our Client Says</h2>
  <div class="quote-card" style="left:163px">
    <div class="avatar" role="img" aria-label="Client portrait"></div>
    <blockquote>Morbi diam mauris viverra in gravida eu mattis in ante Morbi eget arcu Morbi porta libero id ullamcor-per nonummy nibh ligula pulvinar metus eget con-sectetuer augue nisi quis lacus Ut ac mi quis lacus mollis aliquam Curabitur iaculis tempus</blockquote>
    <cite>By Author Name</cite>
  </div>
  <div class="quote-card" style="left:461px">
    <div class="avatar" role="img" aria-label="Client portrait"></div>
    <blockquote>Morbi diam mauris viverra in gravida eu mattis in ante Morbi eget arcu Morbi porta libero id ullamcor-per nonummy nibh ligula pulvinar metus eget con-sectetuer augue nisi quis lacus Ut ac mi quis lacus mollis aliquam Curabitur iaculis tempus</blockquote>
    <cite>By Author Name</cite>
  </div>
  <div class="quote-card" style="left:757px">
    <div class="avatar" role="img" aria-label="Client portrait"></div>
    <blockquote>Morbi diam mauris viverra in gravida eu mattis in ante Morbi eget arcu Morbi porta libero id ullamcor-per nonummy nibh ligula pulvinar metus eget con-sectetuer augue nisi quis lacus Ut ac mi quis lacus mollis aliquam Curabitur iaculis tempus</blockquote>
    <cite>By Author Name</cite>
  </div>
</section>

<footer class="site-footer">
  <nav class="footer-nav">
    <a>Home</a><span class="sep">|</span><a>About Us</a><span class="sep">|</span><a>Services</a><span class="sep">|</span><a>Projects</a><span class="sep">|</span><a>Testimonials</a><span class="sep">|</span><a>Contact</a>
  </nav>
  <div class="copyright">© 2014 Company Name &nbsp;All right reserved &nbsp;Term of Use</div>
  <div class="social"><span>Chirply</span><span>Folkbook</span><span>Linkwork</span></div>
</footer>

</body>
</html>
```